Lumora business card for a plastic surgeon

we need a business card for plastic surgeons that work on a clinic called LUMORA.
we want a clean design and the following informations: name of the doctor, doctor's registration number (called CRM), telephone, address, facebook, instagram.
Colors: white, blue tones, light brown/ coffee

facebook and instagram: lumoracirurgiaestetica

Industry/Entity Type

Business

Contact Information for Business Card

clean design

Font styles to use
Serif
Sans Serif
Other font styles liked:
• helvetica light

Colors
cee9f5
85cae6
85abd2
3276b5
cfeae6
cedeed
eaf1f7

Requirements
Must have
• doctor's name
• identification number (called CRM)
• contact (phone, facebook, instagram, address)

```html
<!DOCTYPE html>
<html lang="en">
<head>
<meta charset="utf-8">
<title>Lumora – Business Card</title>
<link href="https://fonts.googleapis.com/css2?family=Arimo:wght@400&display=swap" rel="stylesheet">
<style>
  :root {
    --backdrop: #050608;
    --card: #ffffff;
    --ink: #111111;
    --blue: #3276b5;
    --blue-deep: #2a72ad;
    --sky: #85cae6;
    --aqua: #2bbcd8;
    --coffee: #a08a78;
  }
  * { margin: 0; padding: 0; box-sizing: border-box; }
  html, body {
    width: 1200px; height: 1170px; overflow: hidden;
    background: var(--backdrop);
    font-family: "Arimo", Helvetica, Arial, sans-serif;
  }
  .card {
    position: absolute;
    left: 294px; width: 629px; height: 359px;
    background: var(--card);
    overflow: hidden;
  }
  .card--front { top: 205px; }
  .card--back { top: 596px; }

  .doctor-name {
    position: absolute; left: 87px; top: 60px;
    font-size: 24px; color: var(--ink); font-weight: 400;
  }
  .registration {
    position: absolute; left: 87px; top: 111px;
    font-size: 17px; color: var(--blue);
  }
  .contact-list { position: absolute; left: 50px; top: 167px; list-style: none; }
  .contact-item {
    position: relative; padding-left: 37px;
    font-size: 14.5px; line-height: 18px; color: var(--coffee);
    margin-bottom: 9.5px;
  }
  .contact-item svg {
    position: absolute; left: 0; top: 1px; width: 16px; height: 16px;
  }
  .contact-item--address { margin-bottom: 10px; }

  .portrait-art {
    position: absolute; right: 0; top: 0; width: 201px; height: 100%;
    background: linear-gradient(90deg, var(--blue-deep) 0%, var(--blue-deep) 45%, var(--sky) 60%, var(--sky) 100%);
  }

  .brand-name {
    position: absolute; left: 0; right: 0; top: 118px;
    text-align: center;
    font-size: 78px; letter-spacing: 6px;
    color: var(--aqua); font-weight: 400;
  }
</style>
</head>
<body>
  <section class="card card--front">
    <h1 class="doctor-name">Dr. Rafael Duarte, M.D.</h1>
    <p class="registration">Identification Number #A101</p>
    <ul class="contact-list">
      <li class="contact-item contact-item--address">
        <svg viewBox="0 0 16 16"><path d="M8 1a4.5 4.5 0 0 0-4.5 4.5C3.5 9 8 12.5 8 12.5S12.5 9 12.5 5.5A4.5 4.5 0 0 0 8 1zm0 6.3a1.8 1.8 0 1 1 0-3.6 1.8 1.8 0 0 1 0 3.6z" fill="var(--blue)"/><ellipse cx="8" cy="14" rx="6" ry="1.5" fill="none" stroke="var(--blue)" stroke-width="1.2"/></svg>
        1420 S 118 HARBOR AVE<br>STATE PIN 48317
      </li>
      <li class="contact-item">
        <svg viewBox="0 0 16 16"><path d="M1.5 6c0-2 3-3.5 6.5-3.5S14.5 4 14.5 6l-3 .8-.6-1.5H5.1l-.6 1.5zM4 8h8l1.5 5h-11z" fill="var(--blue)"/><circle cx="8" cy="10.4" r="1.5" fill="#fff"/></svg>
        (800) 555 - 014 276
      </li>
      <li class="contact-item">
        <svg viewBox="0 0 16 16"><rect x="1" y="3.5" width="14" height="9" fill="var(--blue)"/><path d="M1 3.5l7 5 7-5" fill="none" stroke="#fff" stroke-width="1.2"/></svg>
        contact@lumora.com
      </li>
      <li class="contact-item">
        <svg viewBox="0 0 16 16"><rect x="2" y="2" width="12" height="12" rx="2" fill="var(--blue)"/></svg>
        lumoracirurgiaestetica
      </li>
      <li class="contact-item">
        <svg viewBox="0 0 16 16"><rect x="2" y="2" width="12" height="12" rx="2" fill="var(--blue)"/></svg>
        facebook.com/lumoracirurgiaestetica
      </li>
    </ul>
    <div class="portrait-art" role="img" aria-label="Blue profile silhouettes of a man and a woman facing left"></div>
  </section>

  <section class="card card--back">
    <p class="brand-name">LUMORA</p>
  </section>
</body>
</html>
```